Business Card Design Project - Photographer

Photography business needs a logo. I would like to see creative licence on options on 1 & 2 sided. I really like the concept of a fully / partially frosted design. I have already used ArtHive for my Logo, so I am looking for the same level of assistance with this project.

If you have any questions please let me know

Cheers Dorian

Reason: Unsure why but the duration was not even a day long

Industry/Entity Type

Business

Requirements
Must have
• These are my contact details
Name: Dorian Welcombe
Mobile: 0438 612 907
email: dorian@brightlensstudio.com.au
Website: www.brightlensstudio.com.au
Nice to have
• Facebook: https://www.facebook.com/BrightLensStudioOz

```html
<!DOCTYPE html>
<html lang="en">
<head>
<meta charset="utf-8">
<title>BrightLens Business Card</title>
<link rel="stylesheet" href="https://fonts.googleapis.com/css2?family=Roboto:wght@300;400;700&display=swap">
<style>
  :root {
    --page-bg: #ffffff;
    --card-front-bg: #ffffff;
    --card-border: #8a8a8a;
    --brand-red: #c0272d;
    --red-top: #e83e36;
    --red-bottom: #941a2a;
    --text-white: #ffffff;
    --text-soft: #f4c9cc;
  }
  html, body {
    margin: 0;
    padding: 0;
    width: 1200px;
    height: 1000px;
    overflow: hidden;
    background: var(--page-bg);
    font-family: "Roboto", sans-serif;
  }
  .canvas {
    position: relative;
    width: 1200px;
    height: 1000px;
  }
  .card {
    position: absolute;
    top: 382px;
    width: 413px;
    height: 235px;
    border-radius: 20px;
    box-sizing: border-box;
    overflow: hidden;
  }
  .card-front {
    left: 172px;
    background: var(--card-front-bg);
    border: 1px solid var(--card-border);
    display: flex;
    align-items: center;
    justify-content: center;
  }
  .brand {
    display: flex;
    align-items: center;
    gap: 12px;
  }
  .brand-dot {
    width: 18px;
    height: 18px;
    border-radius: 50%;
    background: var(--brand-red);
  }
  .brand-name {
    font-size: 38px;
    font-weight: 700;
    letter-spacing: 1px;
    color: var(--brand-red);
  }
  .card-back {
    left: 617px;
    background: linear-gradient(to bottom, var(--red-top), var(--red-bottom));
  }
  .die-cut {
    position: absolute;
    left: 180px;
    top: 79px;
    width: 52px;
    height: 52px;
    border-radius: 50%;
    background: var(--page-bg);
  }
  .contact {
    position: absolute;
    left: 0;
    right: 0;
    top: 142px;
    text-align: center;
    font-weight: 300;
    line-height: 22px;
  }
  .contact-name {
    font-size: 19px;
    color: var(--text-white);
  }
  .contact-line {
    font-size: 16.5px;
    color: var(--text-soft);
  }
</style>
</head>
<body>
  <main class="canvas">
    <section class="card card-front" aria-label="Card front">
      <div class="brand">
        <span class="brand-dot"></span>
        <span class="brand-name">BRIGHTLENS</span>
      </div>
    </section>
    <section class="card card-back" aria-label="Card back">
      <span class="die-cut"></span>
      <div class="contact">
        <div class="contact-name">Dorian Welcombe | 0438 612 907</div>
        <div class="contact-line">dorian@brightlensstudio.com.au</div>
        <div class="contact-line">www.brightlensstudio.com.au</div>
      </div>
    </section>
  </main>
</body>
</html>
```